One page website

I'm looking for a landing page for my company. Just a brief description of our medical device technology with some images

Coding

Coded - Design and coding required

```html
<!DOCTYPE html>
<html lang="en">
<head>
<meta charset="utf-8">
<title>Orvex Surgical – Solving Children's Scoliosis</title>
<link href="https://fonts.googleapis.com/css2?family=Poppins:wght@400;500;600;700&family=Arimo:wght@400;700&display=swap" rel="stylesheet">
<style>
:root{
  --blue:#3a9ad9;
  --green:#8cc63f;
  --green-band:#9bc94e;
  --green-soft:#a9c94c;
  --ink:#111;
  --text:#333;
  --muted:#777;
  --red:#e23b3b;
  --pale:#f4f5f6;
  --footer:#2b2b2b;
}
*{box-sizing:border-box;margin:0;padding:0}
html,body{width:1200px;height:4762px;overflow:hidden;background:#fff}
body{position:relative;font-family:"Poppins",sans-serif;color:var(--text)}
.abs{position:absolute}
.sec-title{position:absolute;left:0;width:1200px;text-align:center;font-weight:600;font-size:33px;color:var(--ink);line-height:1.2}
.rule{position:absolute;left:580px;width:40px;height:3px;background:var(--blue)}

/* hero */
.hero-photo{position:absolute;left:0;top:0}
.brand{position:absolute;left:233px;top:70px;font-weight:600;font-size:22px;color:var(--green);display:flex;align-items:center;gap:8px}
.brand-dot{width:12px;height:12px;border-radius:50%;background:var(--blue)}
.phone{position:absolute;left:800px;top:32px;font-weight:600;font-size:19px;color:var(--ink);display:flex;align-items:center;gap:10px}
.hero-title{position:absolute;left:233px;top:208px;font-weight:700;font-size:66px;line-height:76px;color:var(--ink)}

/* mission */
.mission-ring{position:absolute;left:228px;top:578px;width:384px;height:384px;border-radius:50%;background:#8fcdf0}
.mission-ring .g{position:absolute;left:22px;top:22px;width:340px;height:340px;border-radius:50%;background:var(--green)}
.mission-ring .img{position:absolute;left:40px;top:40px;width:304px;height:304px;border-radius:50%;background:radial-gradient(circle at 50% 45%,#c8602d,#8a1c12 55%,#4a0d08)}
.mission-title{position:absolute;left:652px;top:680px;font-weight:600;font-size:31px;color:var(--ink)}
.mission-text{position:absolute;left:652px;top:750px;width:310px;font-size:14px;font-weight:500;line-height:23px;color:var(--ink)}

/* problem */
.problem-bg{position:absolute;left:0;top:925px;width:1200px;height:650px;background:linear-gradient(90deg,#eef0f1,#fafafa 30%,#fff 60%,#f4f5f6)}
.problem-sub{position:absolute;left:0;top:1071px;width:1200px;text-align:center;font-size:12px;font-weight:600;color:var(--ink)}
.xray{position:absolute;top:1128px;width:232px;height:178px}
.xray-label{position:absolute;top:1325px;width:232px;text-align:center;font-weight:600;font-size:19px;color:var(--ink)}
.xray-list{position:absolute;top:1360px;list-style:none;font-size:11.5px;font-weight:600;color:var(--ink)}
.xray-list li{position:relative;padding-left:22px;line-height:22px}
.xray-list li::before{content:"";position:absolute;left:4px;top:8px;width:6px;height:6px;border-radius:50%;background:var(--blue)}
.xray-list .r{color:var(--red)}
.definition{position:absolute;left:233px;top:1440px;width:740px;font-size:10.5px;line-height:13px;color:var(--ink)}
.definition h4{font-size:12px;font-weight:700;text-decoration:underline;margin-bottom:22px}
.definition p{margin-bottom:12px}

/* team */
.member{position:absolute;display:flex;gap:12px;width:190px}
.avatar{flex:none;width:62px;height:62px;border-radius:50%;border:3px solid var(--blue);padding:3px}
.avatar.gr{border-color:var(--green)}
.avatar span{display:block;width:100%;height:100%;border-radius:50%;background:linear-gradient(#c9c3bb,#7a7068)}
.member .info{font-size:8.5px;line-height:10.5px;color:var(--muted)}
.member .name{font-weight:700;color:var(--ink)}
.member .role{color:var(--blue);margin-bottom:5px}
.member .bio{margin-bottom:3px}
.member .stat{font-weight:600;color:var(--ink)}

/* benefits */
.band{position:absolute;left:0;top:2219px;width:1200px;height:438px;background:linear-gradient(90deg,#8fc247,#a0cc55 50%,#93c64b)}
.band-line{position:absolute;left:0;top:2443px;width:1200px;height:2px;background:rgba(255,255,255,.8)}
.benefit-ic{position:absolute;top:2382px;width:124px;height:124px;border-radius:50%;background:var(--blue);border:4px solid #fff;display:flex;align-items:center;justify-content:center}
.benefit-lbl{position:absolute;font-family:"Arimo",sans-serif;font-size:20px;line-height:24px;color:#2f3a20;text-align:center;width:220px}
.benefit-lbl.right{text-align:right;width:300px}
.benefit-lbl small{display:block;font-size:15px;line-height:17px}

/* solution */
.solution-sub{position:absolute;left:0;top:2800px;width:1200px;text-align:center;font-size:12px;font-weight:600;color:var(--ink)}
.checks{position:absolute;left:233px;top:2910px;list-style:none;width:220px}
.checks li{position:relative;padding-left:54px;font-size:13px;line-height:18px;color:var(--ink);height:58px}
.checks li svg{position:absolute;left:0;top:0}
.device{position:absolute;left:471px;top:2931px;width:90px;height:150px;border-radius:6px;background:linear-gradient(135deg,#4ea6d8,#d9e6ee 45%,#8a7c6e)}
.spine{position:absolute;left:679px;top:2883px;width:285px;height:276px;background:linear-gradient(90deg,#28323d,#56626e 45%,#c9b58e 52%,#3f4a56 60%,#222a33)}
.callout{position:absolute;font-size:8.5px;line-height:11px;color:var(--ink)}

/* pig study */
.pig-bg{position:absolute;left:0;top:3240px;width:1200px;height:348px;background:#efefef}
.pig-title{position:absolute;left:233px;top:3285px;font-weight:600;font-size:31px;color:var(--ink)}
.pig-list{position:absolute;left:233px;top:3368px;list-style:none;font-size:12.5px;color:var(--ink)}
.pig-list li{position:relative;padding-left:22px;line-height:30.5px}
.pig-list li::before{content:"";position:absolute;left:4px;top:13px;width:5px;height:5px;border-radius:50%;background:var(--green)}
.pig-img{position:absolute}

/* market */
.market-bg{position:absolute;left:0;top:3744px;width:1200px;height:490px;background:linear-gradient(90deg,#f0f1f2,#fbfbfb 40%,#fff 70%,#f2f3f4)}
.divider{position:absolute;top:3766px;width:1px;height:440px;background:#d8dde0}
.seg{position:absolute;top:3770px;width:360px}
.seg .dot{margin:0 auto;width:114px;height:114px;border-radius:50%;background:var(--green);color:#fff;font-weight:600;font-size:17px;display:flex;align-items:center;justify-content:center}
.seg h3{margin-top:30px;text-align:center;font-family:"Arimo",sans-serif;font-weight:400;font-size:20px;color:var(--green-soft)}
.seg .line{position:relative;margin:12px 0 0 6px;width:340px;height:2px;background:var(--blue)}
.seg .line::after{content:"";position:absolute;left:50%;top:0;margin-left:-32px;border-left:32px solid transparent;border-right:32px solid transparent;border-top:24px solid var(--blue)}
.seg ul{list-style:none;margin:38px 0 0 10px;font-family:"Arimo",sans-serif;font-size:20px;line-height:25px;color:#2e6f9e}
.seg li{position:relative;padding-left:16px;margin-bottom:7px}
.seg li::before{content:"";position:absolute;left:0;top:11px;width:5px;height:5px;border-radius:50%;background:var(--green)}
.seg b{font-weight:700}

/* video */
.video{position:absolute;left:359px;top:4386px;width:482px;height:282px;background:linear-gradient(135deg,#dcdcdc,#b5b5b5 50%,#8d8d8d)}
.play{position:absolute;left:212px;top:93px;width:58px;height:58px;border-radius:50%;background:var(--blue);display:flex;align-items:center;justify-content:center}

.footer{position:absolute;left:0;top:4698px;width:1200px;height:64px;background:var(--footer);color:#ddd;font-size:10px;text-align:center;line-height:64px}
</style>
</head>
<body>

<!-- Hero -->
<svg class="hero-photo" width="1200" height="590" viewBox="0 0 1200 590" role="img" aria-label="Photo of a smiling girl stretching her arms during a clinical spine check">
  <defs>
    <linearGradient id="heroGrad" x1="0" y1="0" x2="1" y2="1">
      <stop offset="0" stop-color="#eef0f2"/>
      <stop offset=".55" stop-color="#d9dde1"/>
      <stop offset="1" stop-color="#bfc6cc"/>
    </linearGradient>
  </defs>
  <path d="M120,0 L1200,0 L1200,410 Q1020,510 900,585 Q720,470 470,340 Q250,210 120,0 Z" fill="url(#heroGrad)"/>
</svg>
<div class="brand"><span class="brand-dot"></span>Orvex Surgical</div>
<div class="phone">
  <svg width="20" height="20" viewBox="0 0 24 24" fill="none" stroke="#3a9ad9" stroke-width="2"><path d="M5 3h4l2 5-3 2a11 11 0 0 0 6 6l2-3 5 2v4a2 2 0 0 1-2 2A17 17 0 0 1 3 5a2 2 0 0 1 2-2z"/></svg>
  555 014 2290
</div>
<h1 class="hero-title">Solving<br>Children's<br>Scoliosis</h1>

<!-- Mission -->
<div class="mission-ring"><div class="g"></div><div class="img" role="img" aria-label="Surgical photo of a tethering implant on the spine"></div></div>
<h2 class="mission-title">Mission</h2>
<div class="rule" style="left:652px;top:728px;width:34px;height:2px"></div>
<p class="mission-text">Develop novel technologies focusing on non-fusion scoliosis correction allowing for non-surgical dynamic adjustment of implants over time</p>

<!-- Problem -->
<div class="problem-bg" role="img" aria-label="Faint medical pattern background"></div>
<h2 class="sec-title" style="top:1004px">Problem</h2>
<p class="problem-sub">Scoliosis affects 2-3% of the population, or an estimated 6-9 million people in the U.S.¹</p>

<div class="xray" style="left:233px;background:radial-gradient(ellipse at 50% 50%,#bfeeea,#3f6d6c 40%,#0f1f20)" role="img" aria-label="X-ray of mild scoliosis"></div>
<div class="xray" style="left:484px;background:radial-gradient(ellipse at 50% 50%,#bfeeea,#3f6d6c 40%,#0f1f20)" role="img" aria-label="X-ray of moderate scoliosis"></div>
<div class="xray" style="left:736px;background:radial-gradient(ellipse at 50% 50%,#c6ead0,#4d7a5a 40%,#14251a)" role="img" aria-label="X-ray of severe scoliosis"></div>

<div class="xray-label" style="left:233px">Mild scoliosis</div>
<ul class="xray-list" style="left:262px"><li>10- to 24-degree Cobb</li><li>Treatment: Monitoring</li></ul>
<div class="xray-label" style="left:484px">Moderate scoliosis</div>
<ul class="xray-list" style="left:508px"><li>25- to 39-degree Cobb</li><li>Treatment: <span class="r">Bracing</span></li></ul>
<div class="xray-label" style="left:736px">Severe scoliosis</div>
<ul class="xray-list" style="left:760px"><li>&gt; 40- to 50-degree Cobb</li><li>Treatment: <span class="r">Fusion</span></li></ul>

<div class="definition">
  <h4>Definition:</h4>
  <p><b>Cobb angle</b> is a term that means the degree of curvature. The Cobb is used to measure the magnitude of spinal deformities, especially in the case of scoliosis.</p>
  <p><b>Scoliosis</b> is considered any lateral (sideways) curvature of the spine that is at least 10 degrees as measured by the Cobb angle, which is found by examining an x-ray of the back</p>
</div>

<!-- Team -->
<h2 class="sec-title" style="top:1592px">Founding Team – Experience in<br>Orthopedic Implants</h2>
<div class="rule" style="top:1682px;height:2px"></div>

<div class="member" style="left:233px;top:1730px"><div class="avatar"><span role="img" aria-label="Portrait"></span></div><div class="info"><div class="name">Owen Castell</div><div class="role">Founder and CEO</div><div class="bio">Co-founder and CEO of a spine implant firm acquired in 2014</div><div class="bio">Leadership roles at two device makers</div></div></div>
<div class="member" style="left:416px;top:1730px"><div class="avatar gr"><span role="img" aria-label="Portrait"></span></div><div class="info"><div class="name">Ravi Mendhar Ph.D.</div><div class="role">Co-Founder Chief Science Officer</div><div class="bio">Previous Chief Scientist at a spine implant firm</div><div class="bio">Leadership roles at two ortho companies</div></div></div>
<div class="member" style="left:604px;top:1730px"><div class="avatar"><span role="img" aria-label="Portrait"></span></div><div class="info"><div class="name">Jonah Ashby</div><div class="role">Co-Founder VP R&amp;D and Operations</div><div class="bio">Previous VP of R&amp;D at a spine firm</div><div class="bio">Leadership roles at three implant makers</div></div></div>
<div class="member" style="left:797px;top:1730px"><div class="avatar gr"><span role="img" aria-label="Portrait"></span></div><div class="info"><div class="name">Dylan Kessler</div><div class="role">Co-founder and Senior R&amp;D Engineer</div><div class="bio">Senior R&amp;D engineer at a university research lab</div></div></div>

<div class="member" style="left:238px;top:1850px"><div class="avatar gr"><span role="img" aria-label="Portrait"></span></div><div class="info"><div class="name">Martin Delacroix, MD</div><div class="role">Professor and Chief of Pediatric Orthopedics</div><div class="stat">60+ tethering procedures performed</div></div></div>
<div class="member" style="left:500px;top:1850px"><div class="avatar"><span role="img" aria-label="Portrait"></span></div><div class="info"><div class="name">Nikhil Arora, MD</div><div class="bio">Professor of Surgery and Director of Spine Trauma at a medical center</div></div></div>
<div class="member" style="left:756px;top:1850px"><div class="avatar gr"><span role="img" aria-label="Portrait"></span></div><div class="info"><div class="name">Dean Calloway, MD</div><div class="bio">Medical Director of a regional spine group and Clinical Professor at a school of medicine</div></div></div>

<div class="member" style="left:364px;top:1946px"><div class="avatar"><span role="img" aria-label="Portrait"></span></div><div class="info"><div class="name">Harold Greer, MD</div><div class="bio">Professor of Surgery and Pediatrics at a children's hospital</div><div class="stat">300+ tethering procedures performed</div></div></div>
<div class="member" style="left:638px;top:1946px"><div class="avatar gr"><span role="img" aria-label="Portrait"></span></div><div class="info"><div class="name">Stefan Hale, MD</div><div class="role">Neurosurgeon at a children's hospital</div><div class="stat">60+ tethering procedures performed</div></div></div>

<!-- Benefits -->
<h2 class="sec-title" style="top:2084px">Benefits - Advantages of VBT<br>over Fusion</h2>
<div class="rule" style="top:2174px;height:2px"></div>
<div class="band" role="img" aria-label="Green band with faint surgical scene"></div>
<div class="band-line"></div>

<div class="benefit-lbl" style="left:30px;top:2280px">Continued<br>skeletal<br>growth</div>
<div class="benefit-lbl" style="left:484px;top:2293px">Single treatment<br>event</div>
<div class="benefit-lbl right" style="left:868px;top:2280px"><b>Does not "burn any bridge":</b><small>fusion remains an unimpacted option<br>if this treatment modality fails</small></div>
<div class="benefit-lbl" style="left:262px;top:2542px">Partial<br>Motion<br>Preservation</div>
<div class="benefit-lbl" style="left:690px;top:2542px;width:240px">Little impact on<br>activity<br>and appearance</div>

<div class="benefit-ic" style="left:79px"><svg width="64" height="64" viewBox="0 0 64 64" fill="#fff"><rect x="10" y="40" width="7" height="14"/><rect x="24" y="32" width="7" height="22"/><rect x="40" y="20" width="7" height="34"/><path d="M43.5 6 54 20H33z"/><path d="M13.5 30l7 9h-14z"/><path d="M27.5 22l7 9h-14z"/></svg></div>
<div class="benefit-ic" style="left:302px"><svg width="64" height="64" viewBox="0 0 64 64" fill="none" stroke="#fff" stroke-width="4"><path d="M6 18V6h12M46 6h12v12M58 46v12H46M18 58H6V46"/><circle cx="32" cy="16" r="4" fill="#fff"/><path d="M32 22l-4 14 6 6-4 12M28 30l-8 4M32 26l8 6 6-2M28 36l-6 10"/></svg></div>
<div class="benefit-ic" style="left:532px"><svg width="64" height="64" viewBox="0 0 64 64" fill="#fff"><path d="M24 6h16v10h10v16H40v10H24V32H14V16h10z"/><path d="M4 46l12-4c4-1 8 0 10 2h10c3 0 3 4 0 4H26h12l14-6c3-1 5 2 2 4L40 56H16L4 60z"/></svg></div>
<div class="benefit-ic" style="left:746px"><svg width="64" height="64" viewBox="0 0 64 64" fill="#fff"><circle cx="32" cy="20" r="12"/><path d="M12 56c0-12 9-20 20-20s20 8 20 20z"/><path d="M20 48h8l3-6 4 10 3-4h8" stroke="#3a9ad9" stroke-width="3" fill="none"/></svg></div>
<div class="benefit-ic" style="left:970px"><svg width="64" height="64" viewBox="0 0 64 64" fill="#fff"><path d="M32 4l12 14h-8v12l14 10v-6l10 10-10 10v-6L36 38v20h-8V38L16 48v6L6 44l10-10v6l12-10V18h-8z"/></svg></div>

<!-- Solution -->
<h2 class="sec-title" style="top:2718px">Solution</h2>
<div class="rule" style="top:2774px;height:2px"></div>
<p class="solution-sub">Orvex Dynamic Tethering System – Magnetic Tensioning</p>

<ul class="checks">
  <li><svg width="38" height="38" viewBox="0 0 38 38"><circle cx="19" cy="19" r="19" fill="#3a9ad9"/><path d="M11 19l6 6 11-12" stroke="#fff" stroke-width="4" fill="none"/></svg>Magnetically activated dynamic tension</li>
  <li><svg width="38" height="38" viewBox="0 0 38 38"><circle cx="19" cy="19" r="19" fill="#3a9ad9"/><path d="M11 19l6 6 11-12" stroke="#fff" stroke-width="4" fill="none"/></svg>Complete non-surgical adjustment</li>
  <li><svg width="38" height="38" viewBox="0 0 38 38"><circle cx="19" cy="19" r="19" fill="#3a9ad9"/><path d="M11 19l6 6 11-12" stroke="#fff" stroke-width="4" fill="none"/></svg>Most effective in making gradual non-surgical adjustments over time</li>
  <li><svg width="38" height="38" viewBox="0 0 38 38"><circle cx="19" cy="19" r="19" fill="#3a9ad9"/><path d="M11 19l6 6 11-12" stroke="#fff" stroke-width="4" fill="none"/></svg>Prevents over-correction and can act as <b>internal brace</b></li>
</ul>

<div class="callout" style="left:471px;top:2900px;font-weight:700">External Magnetic<br>controller</div>
<div class="device" role="img" aria-label="Handheld external magnetic controller"></div>
<div class="callout" style="left:583px;top:2872px">Anchoring screw<br>with cleat<br>mechanism</div>
<div class="callout" style="left:583px;top:3012px">Slider screws</div>
<div class="callout" style="left:483px;top:3117px;width:170px">Magnetic engine attached to vertebral body via screw. Tether wraps around spool. Spool powered via external controller</div>
<div class="spine" role="img" aria-label="Rendering of a spine with tether, screws and magnetic engine"></div>

<!-- Pilot pig study -->
<div class="pig-bg"></div>
<h2 class="pig-title">Pilot Pig Study</h2>
<div class="rule" style="left:233px;top:3336px;width:34px;height:2px"></div>
<ul class="pig-list">
  <li>2 Pigs – 3months old, 25KG</li>
  <li>Xrays every 2 weeks.&nbsp;&nbsp; Adjustments made</li>
  <li>10 weeks total&nbsp;&nbsp; Pigs doubled in size</li>
  <li>Testing system performance and durability</li>
  <li>System remained functioning and intact throughout</li>
</ul>
<div class="pig-img" style="left:653px;top:3291px;width:312px;height:122px;background:radial-gradient(ellipse at 40% 50%,#c8602d,#8a1c12 55%,#3a0b07)" role="img" aria-label="Surgical photo of implanted system"></div>
<div class="pig-img" style="left:653px;top:3434px;width:144px;height:101px;background:radial-gradient(ellipse,#e2e6e8,#7e878c 60%,#40484c)" role="img" aria-label="X-ray of implant"></div>
<div class="pig-img" style="left:820px;top:3434px;width:145px;height:101px;background:radial-gradient(ellipse,#e7eaec,#8a9397 60%,#4a5256)" role="img" aria-label="X-ray of implant"></div>

<!-- Market -->
<h2 class="sec-title" style="top:3639px">Tethering Market Segments</h2>
<div class="rule" style="top:3694px;height:2px"></div>
<div class="market-bg" role="img" aria-label="Faint clinical background"></div>
<div class="divider" style="left:398px"></div>
<div class="divider" style="left:799px"></div>

<div class="seg" style="left:28px">
  <div class="dot">$300M</div>
  <h3>Current Tether Market</h3>
  <div class="line"></div>
  <ul><li>8-12 y/o</li><li>Cobb &gt; 40 degrees</li><li>Growth remaining</li><li>Flexible spine</li><li>10,000 patients</li></ul>
</div>
<div class="seg" style="left:420px">
  <div class="dot">$400M</div>
  <h3>Future Market – AIS Fusion</h3>
  <div class="line"></div>
  <ul><li>10-16 y/o</li><li>Cobb &gt; 40 degrees</li><li>Close to <b>skeletal maturity</b></li><li>Regular "brace-like" adjustments with non-surgical system (magnetic engine)</li><li>30,000 patients</li></ul>
</div>
<div class="seg" style="left:822px">
  <div class="dot">$1B+</div>
  <h3>Future Market – Early Intervention</h3>
  <div class="line"></div>
  <ul><li>Cobb 30-40 degrees</li><li>Never progress to fusion, never wear a brace.</li><li>Develop laparoscopic system</li><li>100K+patients</li></ul>
</div>

<!-- Video -->
<h2 class="sec-title" style="top:4288px">Video of Martin Delacroix, MD</h2>
<div class="rule" style="top:4344px;height:2px"></div>
<div class="video" role="img" aria-label="Video still: rendering of a spine with tether and dynamic adjustment">
  <div class="play"><svg width="22" height="24" viewBox="0 0 22 24"><path d="M2 1l19 11L2 23z" fill="#fff"/></svg></div>
</div>

<footer class="footer">Copyright © Orvex Surgical 2020, All Rights Reserved.</footer>

</body>
</html>
```